Zuvex Template Design in Baby Category

We are a maternity/baby store on Zuvex in need of a store front design template (Store front, listing and detail page page) that is accustom to our category, is user friendly, easy to read and navigate and mobile friendly.

The design should be reflecting a motherhood warm feeling with a modern look.

Please don't hesitate to inquire, if you need any clarification.

Thank you

Industry/Entity Type

Baby

Number of Pages Required

3 page

```html
<!DOCTYPE html>
<html lang="en">
<head>
<meta charset="utf-8">
<title>Zuvex Baby Store</title>
<link rel="stylesheet" href="https://fonts.googleapis.com/css2?family=Lato:wght@400;700;900&family=Cinzel:wght@400&display=swap">
<style>
:root{
  --red:#d9131c;
  --dark:#2a2a2a;
  --darker:#141414;
  --ink:#222;
  --muted:#666;
  --line:#d6d6d6;
  --page:#fbf8f9;
  --band:#e4e4e4;
  --yellow:#f5c400;
  --white:#fff;
}
*{box-sizing:border-box;margin:0;padding:0}
html,body{width:730px;height:1200px;overflow:hidden}
body{position:relative;background:var(--page);font-family:"Lato",Arial,sans-serif;color:var(--ink)}
.abs{position:absolute}
a{color:inherit;text-decoration:none}

/* top bar */
.topbar{left:0;top:0;width:730px;height:18px;background:var(--dark)}
.toplinks{right:130px;top:0;height:18px;display:flex;font-size:6px;font-weight:700;color:var(--white)}
.toplinks a{display:flex;align-items:center;gap:3px;padding:0 6px;border-left:1px solid #555}
.toplinks i{width:4px;height:4px;background:var(--red);border-radius:50%;display:block}

/* header */
.header{left:0;top:18px;width:730px;height:36px;background:var(--white)}
.logo{left:128px;top:22px;font-family:"Cinzel",Georgia,serif;font-size:20px;color:var(--red);text-transform:none}
.search{left:268px;top:28px;width:161px;height:14px;border:1px solid #999;font-size:5px;color:#777;padding:3px 5px;font-style:italic}
.search svg{position:absolute;right:3px;top:3px}
.phone{left:476px;top:30px;font-size:6px;color:#444;display:flex;gap:6px;align-items:center}
.cart{left:542px;top:27px;width:52px;height:15px;border:1px solid #aaa;font-size:5px;color:#555;display:flex;align-items:center;gap:7px;padding-left:5px}

/* nav */
.nav{left:0;top:54px;width:730px;height:21px;background:var(--red);border-top:1px solid #b80d15}
.nav ul{position:absolute;left:128px;top:0;display:flex;list-style:none;height:21px}
.nav li{font-size:5px;font-weight:700;color:var(--white);text-transform:uppercase;display:flex;align-items:center;justify-content:center;border-right:1px solid #ef5a60;height:21px}
.nav li.active{background:var(--white);color:var(--ink);height:22px}

/* sidebar */
.sidebar{left:128px;top:76px;width:111px;height:424px;background:var(--white);border:1px solid var(--line)}
.side-title{position:absolute;left:4px;width:102px;height:18px;border:1px solid #999;font-size:10px;text-align:center;line-height:16px;color:#333}
.side-list{position:absolute;left:7px;list-style:none}
.side-list li{font-size:5px;height:13px;line-height:13px;display:flex;gap:4px;align-items:center;color:#333}
.side-list li::before{content:"";border-left:3px solid #999;border-top:2.5px solid transparent;border-bottom:2.5px solid transparent}

/* content */
.content{left:243px;top:76px;width:358px;height:530px;background:var(--white);border:1px solid var(--line)}
.slider{left:249px;top:76px;width:347px;height:164px;background:linear-gradient(160deg,#b7939f,#d9c3c6 45%,#a88a93)}
.slide-arrow{top:143px;width:16px;height:14px;background:#444;opacity:.85;display:flex;align-items:center;justify-content:center}
.section-title{left:250px;top:250px;font-size:9px;color:#333}

.card{width:107px;height:151px;background:var(--white);border:1px solid var(--line)}
.card .photo{position:absolute;left:0;top:0;width:105px;height:82px;border-bottom:1px solid var(--line)}
.card .tag{position:absolute;right:0;top:0}
.card h3{position:absolute;left:10px;top:90px;font-size:6px;font-weight:700}
.card p{position:absolute;left:10px;top:101px;width:88px;font-size:4.6px;font-weight:700;line-height:6px;color:#333}
.price{position:absolute;left:10px;top:126px;display:flex;height:14px;font-size:5.5px;font-weight:700;color:var(--white)}
.price span{background:var(--dark);width:30px;display:flex;align-items:center;justify-content:center}
.price b{background:var(--red);width:29px;display:flex;align-items:center;justify-content:center;gap:3px}

/* gallery */
.tile{border:1px solid #ccc}

/* features */
.features{left:129px;top:816px;width:474px;height:42px;background:var(--band)}
.feature{position:absolute;top:7px;display:flex;gap:6px}
.feature .icon{width:32px;height:28px;background:var(--white);border:1px solid #999;display:flex;align-items:center;justify-content:center}
.feature h4{font-size:7px;font-weight:400;color:#333;margin-top:1px}
.feature p{font-size:4.8px;font-weight:700;line-height:6px;margin-top:3px;width:110px}

/* promo */
.promo-photo{left:129px;top:867px;width:309px;height:171px;background:linear-gradient(120deg,#8fb05a,#d9c7b0 40%,#c9a7a0 70%,#9a8b7f)}
.promo{left:438px;top:867px;width:165px;height:171px;background:var(--dark);color:var(--white)}
.promo h2{position:absolute;left:25px;top:22px;font-size:15px;font-weight:900;letter-spacing:.2px}
.promo .l1{position:absolute;left:26px;top:46px;font-size:11px}
.promo .l2{position:absolute;left:26px;top:71px;font-size:10px}
.promo em{font-style:normal;color:var(--red)}
.promo .l2 em{color:var(--yellow)}
.promo .l3{position:absolute;left:26px;top:98px;font-size:7px;font-weight:700;color:var(--yellow)}
.shop-btn{position:absolute;left:26px;top:124px;height:14px;display:flex;font-size:5px;font-weight:700}
.shop-btn i{width:17px;background:#ef4a50;display:flex;align-items:center;justify-content:center}
.shop-btn span{width:38px;background:var(--red);display:flex;align-items:center;justify-content:center}

/* footer */
.footer{left:0;top:1038px;width:730px;height:138px;background:var(--dark);color:var(--white)}
.fcol{position:absolute;top:14px}
.fcol h5{font-size:8.5px;font-weight:900;text-transform:uppercase;margin-bottom:8px}
.fcol ul{list-style:none}
.fcol li{font-size:5.5px;height:13px;display:flex;align-items:center;gap:5px;color:#ddd}
.arrow-list li::before{content:"";border-left:3px solid #999;border-top:2.5px solid transparent;border-bottom:2.5px solid transparent}
.socials{display:flex;gap:2px;margin-top:2px}
.socials i{width:10px;height:10px;border-radius:50%;background:#888;display:block}
.socials i:last-child{background:var(--red)}
.field{width:97px;height:14px;background:#555;font-size:5px;color:#ccc;padding:4px 4px;margin-bottom:2px}
.submit{margin-top:7px;width:40px;height:13px;background:var(--white);color:var(--ink);font-size:5.5px;font-weight:900;display:flex;align-items:center;justify-content:center}
.copyright{left:0;top:1176px;width:730px;height:24px;background:var(--darker);color:#ddd;font-size:5px;text-align:center;line-height:26px}
</style>
</head>
<body>

<div class="abs topbar"></div>
<nav class="abs toplinks">
  <a href="#"><i></i>My Account</a>
  <a href="#"><i></i>Wishlist</a>
  <a href="#"><i></i>Checkout</a>
  <a href="#"><i></i>Login</a>
</nav>

<header class="abs header"></header>
<div class="abs logo">Logo</div>
<div class="abs search">Search the product...
  <svg width="7" height="7" viewBox="0 0 10 10"><circle cx="4" cy="4" r="3" fill="none" stroke="#666" stroke-width="1.3"/><path d="M6.3 6.3 9 9" stroke="#666" stroke-width="1.3"/></svg>
</div>
<div class="abs phone">
  <svg width="8" height="8" viewBox="0 0 10 10"><path d="M2 1l2 2-1 1.3c.7 1.3 1.5 2.1 2.7 2.7L7 6l2 2-1.3 1.3C4.5 9 1 5.5.7 2.3z" fill="#555"/></svg>
  123 456 7890
</div>
<div class="abs cart">
  <svg width="10" height="8" viewBox="0 0 12 10"><path d="M0 1h2l1.5 5h6L11 2.5H3" fill="none" stroke="#777" stroke-width="1"/><circle cx="4.5" cy="8.3" r=".9" fill="#777"/><circle cx="8.5" cy="8.3" r=".9" fill="#777"/></svg>
  <span style="border-left:1px solid #bbb;padding-left:6px">My Cart</span>
</div>

<nav class="abs nav">
  <ul>
    <li class="active" style="width:71px">Home</li>
    <li style="width:75px">Info</li>
    <li style="width:57px">Store</li>
    <li style="width:97px">Custom Clothing</li>
    <li style="width:79px">Accessories</li>
    <li style="width:83px;border-right:none">Contact Us</li>
  </ul>
</nav>

<aside class="abs sidebar">
  <div class="side-title" style="top:14px">Product Categories</div>
  <ul class="side-list" style="top:39px">
    <li>Lorem Ipsum is simply</li><li>Lorem Ipsum is simply Lorem Ipsum</li><li>Lorem Ipsum is simply</li>
    <li>Lorem Ipsum is simply Lorem Ipsum</li><li>Lorem Ipsum is simply Lorem Ipsum</li><li>Lorem Ipsum is simply Lorem</li>
  </ul>
  <div class="side-title" style="top:124px">Information</div>
  <ul class="side-list" style="top:149px">
    <li>Lorem Ipsum is simply</li><li>Lorem Ipsum is simply Lorem Ipsum</li><li>Lorem Ipsum is simply</li>
    <li>Lorem Ipsum is simply Lorem Ipsum</li><li>Lorem Ipsum is simply Lorem Ipsum</li><li>Lorem Ipsum is simply Lorem</li>
    <li>Lorem Ipsum is simply</li><li>Lorem Ipsum is simply Lorem Ipsum</li><li>Lorem Ipsum is simply Lorem Ipsum</li>
    <li>Lorem Ipsum is simply Lorem</li>
  </ul>
  <div class="side-title" style="top:293px">Baby Needs</div>
  <ul class="side-list" style="top:318px">
    <li>Lorem Ipsum is simply</li><li>Lorem Ipsum is simply Lorem Ipsum</li><li>Lorem Ipsum is simply</li>
    <li>Lorem Ipsum is simply Lorem Ipsum</li><li>Lorem Ipsum is simply Lorem Ipsum</li><li>Lorem Ipsum is simply Lorem</li>
    <li>Lorem Ipsum is simply</li>
  </ul>
</aside>

<main class="abs content"></main>
<div class="abs slider" role="img" aria-label="Baby wrapped in a soft hooded towel"></div>
<div class="abs slide-arrow" style="left:249px"><svg width="5" height="6" viewBox="0 0 5 6"><path d="M4 0 1 3l3 3" fill="none" stroke="#fff"/></svg></div>
<div class="abs slide-arrow" style="left:580px"><svg width="5" height="6" viewBox="0 0 5 6"><path d="M1 0l3 3-3 3" fill="none" stroke="#fff"/></svg></div>
<div class="abs section-title">Product</div>

<!-- product cards -->
<div class="abs card" style="left:249px;top:272px">
  <div class="photo" role="img" aria-label="Baby care gift set" style="background:linear-gradient(135deg,#f3e6d0,#e9b6a6)"></div>
  <svg class="tag" width="22" height="22"><path d="M0 0h22v22z" fill="var(--red)"/></svg>
  <h3>Lorem Ipsum is simply Lorem</h3><p>Lorem Ipsum is simply dummy text of the printing and typesetting industry.</p>
  <div class="price"><span>$20</span><b><svg width="5" height="4" viewBox="0 0 12 10"><path d="M0 1h2l1.5 5h6L11 2.5H3" fill="none" stroke="#fff" stroke-width="1.5"/></svg>Bye</b></div>
</div>
<div class="abs card" style="left:369px;top:272px">
  <div class="photo" role="img" aria-label="Baby feeding bottle and bib" style="background:linear-gradient(135deg,#e8eef6,#9fc3e8)"></div>
  <svg class="tag" width="22" height="22"><path d="M0 0h22v22z" fill="var(--red)"/></svg>
  <h3>Lorem Ipsum is simply Lorem</h3><p>Lorem Ipsum is simply dummy text of the printing and typesetting industry.</p>
  <div class="price"><span>$20</span><b><svg width="5" height="4" viewBox="0 0 12 10"><path d="M0 1h2l1.5 5h6L11 2.5H3" fill="none" stroke="#fff" stroke-width="1.5"/></svg>Bye</b></div>
</div>
<div class="abs card" style="left:488px;top:272px">
  <div class="photo" role="img" aria-label="Wooden crib organiser" style="background:linear-gradient(135deg,#d9c8b6,#7a5a44)"></div>
  <svg class="tag" width="22" height="22"><path d="M0 0h22v22z" fill="var(--red)"/></svg>
  <h3>Lorem Ipsum is simply Lorem</h3><p>Lorem Ipsum is simply dummy text of the printing and typesetting industry.</p>
  <div class="price"><span>$20</span><b><svg width="5" height="4" viewBox="0 0 12 10"><path d="M0 1h2l1.5 5h6L11 2.5H3" fill="none" stroke="#fff" stroke-width="1.5"/></svg>Bye</b></div>
</div>
<div class="abs card" style="left:249px;top:450px">
  <div class="photo" role="img" aria-label="Hanging diaper caddy" style="background:linear-gradient(135deg,#f3efe3,#d8cfa8)"></div>
  <svg class="tag" width="22" height="22"><path d="M0 0h22v22z" fill="var(--red)"/></svg>
  <h3>Lorem Ipsum is simply Lorem</h3><p>Lorem Ipsum is simply dummy text of the printing and typesetting industry.</p>
  <div class="price"><span>$20</span><b><svg width="5" height="4" viewBox="0 0 12 10"><path d="M0 1h2l1.5 5h6L11 2.5H3" fill="none" stroke="#fff" stroke-width="1.5"/></svg>Bye</b></div>
</div>
<div class="abs card" style="left:369px;top:450px">
  <div class="photo" role="img" aria-label="Crib side storage bag" style="background:linear-gradient(135deg,#efe7df,#a87a58)"></div>
  <svg class="tag" width="22" height="22"><path d="M0 0h22v22z" fill="var(--red)"/></svg>
  <h3>Lorem Ipsum is simply Lorem</h3><p>Lorem Ipsum is simply dummy text of the printing and typesetting industry.</p>
  <div class="price"><span>$20</span><b><svg width="5" height="4" viewBox="0 0 12 10"><path d="M0 1h2l1.5 5h6L11 2.5H3" fill="none" stroke="#fff" stroke-width="1.5"/></svg>Bye</b></div>
</div>
<div class="abs card" style="left:488px;top:450px">
  <div class="photo" role="img" aria-label="Fabric wall organiser with pockets" style="background:linear-gradient(135deg,#cdbfc0,#6e5c5f)"></div>
  <svg class="tag" width="22" height="22"><path d="M0 0h22v22z" fill="var(--red)"/></svg>
  <h3>Lorem Ipsum is simply Lorem</h3><p>Lorem Ipsum is simply dummy text of the printing and typesetting industry.</p>
  <div class="price"><span>$20</span><b><svg width="5" height="4" viewBox="0 0 12 10"><path d="M0 1h2l1.5 5h6L11 2.5H3" fill="none" stroke="#fff" stroke-width="1.5"/></svg>Bye</b></div>
</div>

<!-- gallery -->
<div class="abs tile" role="img" aria-label="Beige baby stroller" style="left:129px;top:632px;width:134px;height:170px;background:linear-gradient(160deg,#5a3a2a,#8b6a55 60%,#d8cbb8)"></div>
<div class="abs tile" role="img" aria-label="Teddy bears and toys in a basket" style="left:265px;top:632px;width:200px;height:84px;background:linear-gradient(120deg,#6b4a30,#b3392e 50%,#7a5a3c)"></div>
<div class="abs tile" role="img" aria-label="Pink toy chest with colourful blocks" style="left:265px;top:718px;width:200px;height:84px;background:linear-gradient(180deg,#c9b6a4,#b05878 55%,#8a6648)"></div>
<div class="abs tile" role="img" aria-label="Crib organiser filled with baby clothes" style="left:468px;top:632px;width:134px;height:170px;background:linear-gradient(160deg,#e8e2dc,#b08a6a 50%,#6a4a36)"></div>

<!-- features -->
<section class="abs features">
  <div class="feature" style="left:5px">
    <div class="icon"><svg width="18" height="12" viewBox="0 0 18 12"><path d="M1 1h10v8H1zM11 4h4l2 3v2h-6z" fill="#666"/><circle cx="4" cy="10" r="1.6" fill="#666" stroke="#fff"/><circle cx="14" cy="10" r="1.6" fill="#666" stroke="#fff"/></svg></div>
    <div><h4>Free Shipping</h4><p>Lorem Ipsum is simply dummy text of the printing and typesetting industry.</p></div>
  </div>
  <div class="feature" style="left:165px">
    <div class="icon"><svg width="14" height="14" viewBox="0 0 14 14"><circle cx="7" cy="7" r="5.5" fill="none" stroke="#555" stroke-width="1.6"/><path d="M7 4v3.5l2.5 1.5" fill="none" stroke="#555" stroke-width="1.6"/></svg></div>
    <div><h4>Order</h4><p>Lorem Ipsum is simply dummy text of the printing and typesetting industry.</p></div>
  </div>
  <div class="feature" style="left:324px">
    <div class="icon"><svg width="14" height="12" viewBox="0 0 14 12"><path d="M1 6l4 4 8-9" fill="none" stroke="#555" stroke-width="2.6"/></svg></div>
    <div><h4>Check Out</h4><p>Lorem Ipsum is simply dummy text of the printing and typesetting industry.</p></div>
  </div>
</section>

<!-- promo -->
<div class="abs promo-photo" role="img" aria-label="Toddlers playing together with toys on a mat"></div>
<section class="abs promo">
  <h2>SHOP THE LOOK</h2>
  <div class="l1">Over <em>5000</em> product</div>
  <div class="l2">UPTO <em>70% OFF</em></div>
  <div class="l3">Baby Storage</div>
  <a class="shop-btn" href="#"><i><svg width="8" height="4" viewBox="0 0 8 4"><path d="M0 2h7M5 0l2 2-2 2" fill="none" stroke="#fff" stroke-width=".8"/></svg></i><span>Shop Now</span></a>
</section>

<!-- footer -->
<footer class="abs footer">
  <div class="fcol" style="left:133px">
    <h5>Main Menu</h5>
    <ul class="arrow-list"><li>Home</li><li>Info</li><li>Store</li><li>Custom clothing</li><li>Accessories</li><li>Contact us</li></ul>
  </div>
  <div class="fcol" style="left:236px">
    <h5>Quick Links</h5>
    <ul class="arrow-list"><li>Customer Policy</li><li>Pvt Policy</li><li>Terms and conditions of use</li><li>Secure payment</li><li>Site map</li></ul>
  </div>
  <div class="fcol" style="left:385px">
    <h5>Services</h5>
    <ul><li>Sell online</li><li>Baby Storage</li></ul>
    <h5 style="margin-top:10px">Follow Us On</h5>
    <div class="socials"><i></i><i></i><i></i><i></i></div>
  </div>
  <div class="fcol" style="left:499px">
    <h5>Newsletter</h5>
    <div style="font-size:5.5px;color:#ddd;margin:-1px 0 8px">Lorem ipsum dolor sit amet</div>
    <div class="field">Your name</div>
    <div class="field">Email id</div>
    <div class="submit">SUBMIT</div>
  </div>
</footer>
<div class="abs copyright">Copyright ©2015 Zuvex. All Rights Reserved.</div>

</body>
</html>
```